Brackenford Hearing Clinic Business Card Design Project

We need a new business card design. We changed our logo recently and need to update our cards. We are a small hearing clinic with a 3 locations in BC. We help people with hearing loss by fitting them with hearing instruments that are appropriate for them and help them overcome the challenges that hearing loss causes. The symbol part of our logo represents the three important components of successful outcome. The three are: 1-acceptance of the change in hearing, 2-a hearing care provider that cares and is knowledgeable and experienced, 3-a quality hearing instrument. I would like to have a clean design that shows quality commitment to a successful end result of treatment. Here is our website for more information. www.earlumo.ca

Target Market(s)

Senior population - mostly 50+

Industry/Entity Type

Clinic

Requirements
Must have
• Logo
Name - Devon Pallister
Title - Hearing Instrument Practitioner (can be very small)
Phone: 250 637-4819
Address: 415-B 22nd Street, Alder Bay, BC V0N 7T2
Email: devon@earlumo.ca
website address: www.earlumo.ca
Nice to have
• Could be both sided and have a photo on the card.

```html
<!DOCTYPE html>
<html lang="en">
<head>
<meta charset="utf-8">
<title>Brackenford Hearing Clinic – Business Card</title>
<link rel="stylesheet" href="https://fonts.googleapis.com/css2?family=Roboto+Condensed:wght@400;500&family=Saira+Condensed:wght@500&display=swap">
<style>
  :root {
    --page: #e9e6e2;
    --card: #000000;
    --glow: #444444;
    --orange: #f0962a;
    --blue: #3f72d6;
    --photo-warm: #b8661f;
    --photo-deep: #5a2a12;
  }
  * { margin: 0; padding: 0; box-sizing: border-box; }
  html, body { width: 1200px; height: 1200px; overflow: hidden; }
  body {
    background: var(--page);
    position: relative;
    font-family: "Roboto Condensed", "Arial Narrow", sans-serif;
  }
  .card {
    position: absolute;
    left: 265px;
    width: 647px;
    height: 373px;
    background: var(--card);
    overflow: hidden;
  }
  .card--front {
    top: 170px;
    background: radial-gradient(ellipse 260px 300px at 120px 150px, var(--glow), var(--card) 100%);
  }
  .card--back {
    top: 618px;
    background: radial-gradient(ellipse 280px 150px at 310px 20px, var(--glow), var(--card) 100%);
  }
  .photo {
    position: absolute;
    left: 35px; top: 104px;
    width: 186px; height: 166px;
    border: 2px solid #1a1a1a;
    background: linear-gradient(135deg, var(--photo-warm), var(--photo-deep));
  }
  .brand {
    position: absolute;
    display: flex;
    align-items: center;
    gap: 9px;
    color: var(--blue);
    font-weight: 500;
    white-space: nowrap;
  }
  .brand__dot {
    width: 30px; height: 30px;
    border-radius: 50%;
    background: var(--orange);
    flex: none;
  }
  .card--front .brand { left: 270px; top: 186px; font-size: 27px; }
  .card--back .brand { left: 193px; top: 84px; font-size: 25px; }
  .person {
    position: absolute;
    left: 253px; top: 134px;
    color: var(--orange);
    white-space: nowrap;
  }
  .person__name {
    font-family: "Saira Condensed", "Arial Narrow", sans-serif;
    font-weight: 500;
    font-size: 29px;
  }
  .person__title {
    font-family: "Saira Condensed", "Arial Narrow", sans-serif;
    font-size: 11px;
    margin-left: 3px;
  }
  .contact {
    position: absolute;
    left: 0; right: 0;
    text-align: center;
    color: var(--orange);
    font-size: 15px;
    line-height: 19px;
  }
  .contact--address { top: 187px; }
  .contact--phone { top: 233px; }
  .contact--email { top: 259px; }
  .contact--web { top: 346px; font-size: 16px; }
  .contact svg { vertical-align: -3px; margin-right: 6px; }
</style>
</head>
<body>
  <section class="card card--front">
    <div class="photo" role="img" aria-label="Portrait photo of the clinic's two practitioners standing in the clinic hallway"></div>
    <div class="brand"><span class="brand__dot"></span>Brackenford Hearing Clinic</div>
  </section>

  <section class="card card--back">
    <div class="brand"><span class="brand__dot"></span>Brackenford Hearing Clinic</div>
    <div class="person">
      <span class="person__name">Devon Pallister</span><span class="person__title">Hearing Instrument Practitioner</span>
    </div>
    <p class="contact contact--address">415-B 22nd Street, Alder Bay,<br>BC V0N 7T2</p>
    <p class="contact contact--phone">
      <svg width="12" height="16" viewBox="0 0 12 16" aria-hidden="true"><path d="M3 1 L5 4 L3.5 5.5 C4 8 5.5 10.5 7.5 12 L9 10.5 L11.5 12.5 L9.5 15 C5 14 1 8 1 2.5 Z" fill="var(--orange)"/></svg>250 637-4819
    </p>
    <p class="contact contact--email">
      <svg width="16" height="11" viewBox="0 0 16 11" aria-hidden="true"><rect x="0" y="0" width="16" height="11" fill="var(--orange)"/><path d="M0 0 L8 6 L16 0" stroke="#000" stroke-width="1.2" fill="none"/></svg>devon@earlumo.ca
    </p>
    <p class="contact contact--web">www.earlumo.ca</p>
  </section>
</body>
</html>
```